Business card for different employees

A professional new updated design incorporating our current business's color themes and styles such as our on-site service trucks decals included in pictures attached. Our current business card is very simple and not professionally designed. We are a small family business but want a professional corporate look.

Target Market(s)

Cards to be handed out to new customers , corperate meetings. For our on site service operators.

Industry/Entity Type

Hydraulic

Contact Information for Business Card

Address, website, phone number, email, logo.
slogan - "Industry chosen hose and fittings provider".
24/7 on-site service , supply and hose management
Experienced , indpendant , family owned

Font styles to use
Sans Serif

Requirements
Must have
• Easily editable so that I can add different names and different roles for employees etc.
Nice to have
• Freedom with colour doesn't necessarily have to be blue but that is our company colour theme with trucks and logo so makes sense for the card to have blue like the trucks.

```html
<!DOCTYPE html>
<html lang="en">
<head>
<meta charset="utf-8">
<title>Meridian Hose and Fittings – Business Card</title>
<link href="https://fonts.googleapis.com/css2?family=Montserrat:wght@800&family=Saira+Condensed:wght@600&family=Barlow:wght@400;500&display=swap" rel="stylesheet">
<style>
  :root {
    --backdrop: #1f1f1f;
    --brand-blue: #2f45a0;
    --brand-blue-text: #2b41b4;
    --ink: #111111;
    --paper: #ffffff;
    --muted: #222222;
  }
  * { box-sizing: border-box; margin: 0; padding: 0; }
  html, body {
    width: 1200px; height: 900px; overflow: hidden;
    background: var(--backdrop);
  }
  .canvas {
    width: 1200px; height: 900px;
    display: flex; flex-direction: column; align-items: center; justify-content: center;
    gap: 40px;
  }
  .card {
    width: 700px; height: 400px; position: relative; overflow: hidden;
    box-shadow: 0 10px 30px rgba(0,0,0,.5);
  }

  /* Front */
  .card--front { background: var(--brand-blue); color: var(--paper); }
  .brand {
    display: flex; align-items: center; gap: 14px;
    font-family: "Montserrat", sans-serif; font-weight: 800;
    text-transform: uppercase; letter-spacing: 2px;
  }
  .brand__dot { width: 54px; height: 54px; border-radius: 50%; background: var(--ink); flex: none; }
  .brand__name { font-size: 30px; line-height: 1.05; }
  .brand__name small { display: block; font-size: 15px; letter-spacing: 5px; }
  .card--front .brand { position: absolute; top: 60px; left: 120px; color: var(--paper); }
  .taglines {
    position: absolute; left: 0; right: 0; top: 228px;
    font-family: "Montserrat", sans-serif; font-weight: 800; text-transform: uppercase;
    font-size: 17px; letter-spacing: 2px; text-align: center; line-height: 1;
  }
  .taglines p { padding: 8px 0; }
  .taglines .band { background: var(--paper); color: var(--brand-blue); }

  /* Back */
  .card--back { background: var(--paper); color: var(--muted); }
  .card--back .brand { position: absolute; top: 60px; right: 60px; color: var(--brand-blue-text); }
  .card--back .brand__dot { background: var(--ink); }
  .person { position: absolute; left: 50px; top: 268px; text-align: right; width: 190px; }
  .person__name {
    font-family: "Saira Condensed", sans-serif; font-weight: 600; font-size: 36px;
    color: var(--brand-blue-text); text-transform: uppercase; line-height: 1;
  }
  .person__role { font-family: "Barlow", sans-serif; font-size: 20px; margin-top: 6px; }
  .divider { position: absolute; width: 2px; height: 82px; background: var(--brand-blue-text); top: 270px; }
  .divider--a { left: 268px; }
  .divider--b { left: 540px; }
  .contact {
    position: absolute; left: 292px; top: 266px; list-style: none;
    font-family: "Barlow", sans-serif; font-size: 19px; line-height: 30px;
  }
  .contact li { display: flex; align-items: center; gap: 10px; }
  .contact svg { width: 18px; height: 18px; flex: none; }
  .contact .accent { color: var(--brand-blue-text); }
  .address {
    position: absolute; left: 566px; top: 272px;
    font-family: "Barlow", sans-serif; font-size: 19px; line-height: 26px;
  }
</style>
</head>
<body>
<main class="canvas">
  <section class="card card--front" aria-label="Card front">
    <div class="brand">
      <span class="brand__dot"></span>
      <span class="brand__name">Meridian<small>Hose and Fittings</small></span>
    </div>
    <div class="taglines">
      <p>Industry chosen hose and fittings provider</p>
      <p class="band">24/7 on-site service . supply and hose management</p>
      <p>Experienced . indpendant . family owned</p>
    </div>
  </section>

  <section class="card card--back" aria-label="Card back">
    <div class="brand">
      <span class="brand__dot"></span>
      <span class="brand__name">Meridian<small>Hose and Fittings</small></span>
    </div>
    <div class="person">
      <p class="person__name">Daniel Corrow</p>
      <p class="person__role">Owner/ CEO</p>
    </div>
    <span class="divider divider--a"></span>
    <ul class="contact">
      <li>
        <svg viewBox="0 0 24 24" fill="none" stroke="var(--brand-blue-text)" stroke-width="1.8"><circle cx="12" cy="12" r="10"/><path d="M8.5 7.5c0 4.5 3.5 8 8 8l1-2-2.5-1-1 1c-1.5-.6-2.9-2-3.5-3.5l1-1-1-2.5z"/></svg>
        0400 123 456
      </li>
      <li>
        <svg viewBox="0 0 24 24" fill="none" stroke="var(--brand-blue-text)" stroke-width="1.8"><rect x="2" y="5" width="20" height="14"/><path d="M2 5l10 8 10-8"/></svg>
        meridianhose@mail.com
      </li>
      <li>
        <svg viewBox="0 0 24 24" fill="none" stroke="var(--brand-blue-text)" stroke-width="1.8"><circle cx="12" cy="12" r="10"/><ellipse cx="12" cy="12" rx="4" ry="10"/><path d="M2 12h20M4 7h16M4 17h16"/></svg>
        <span>www.<span class="accent">meridianhose</span>.com.au</span>
      </li>
    </ul>
    <span class="divider divider--b"></span>
    <address class="address" style="font-style:normal">
      48 Calder Ct.<br>Suite 200<br>AU 3061
    </address>
  </section>
</main>
</body>
</html>
```